Crestline Delivery Partners Business Card Redesign Project

CRESTLINE DELIVERY PARTNERS
Our company needs to have its business cards redesigned as the current design no longer reflects the business brand or attracts the type of clientele we are seeking.

MUST LOOK
★ Upmarket
★ Reflect Quality
★ Corporate feel
★ Professional
★ Innovative
★ Colourful

MUST PROMOTE
★ Market Leader
★ Knowledge
★ Expertise
★ Experience
★ Solutions
★ Advice

MUST FEEL
★ Classy
★ Elegant
★ Savvy
★ Edgy
★ Upbeat

WHAT WE DO
Crestline Delivery Partners provides project management and project controls consultancy services to companies in many industry sectors, within Australia and overseas. My company has developed a business brand through forging strong business relationships within industry. We provide innovative tools, concepts and solutions to management teams to assist them in better plan and managing there project portfolios.

SECTORS OF INDUSTRY WE SERVICE
★Oil & Gas
★Minerals & Metals
★Petrochemical
★Manufacturing
★Building & Construction
★Telecommunications
★Rail
★Civil

BUSINESS CARD DETAILS REQUIRED ON FRONT
Marcus Feldwick
Business Owner
Tel: 0498357162
Email: marcusfeldwick@crestlinedeliverypartners.com
Website: www.crestlinedeliverypartners.com.au

BUSINESS CARD DETAILS REQUIRED ON BACK
Providing | Knowledge | Expertise | Experience

ATTACHMENTS
Business Logo

Target Market(s)

Oil & Gas I Mining & Resources I Industry in General
Upmarket Clientele
Corporate World

Industry/Entity Type

Industry

Requirements
Must have
• Must be creative and a unique design
The business card must have information on the front and back

```html
<!DOCTYPE html>
<html lang="en">
<head>
<meta charset="utf-8">
<title>Crestline Delivery Partners – Business Card</title>
<link href="https://fonts.googleapis.com/css2?family=Ubuntu:wght@400;500;700&display=swap" rel="stylesheet">
<style>
  :root {
    --board: #ffffff;
    --ink: #1a1a1a;
    --ink-soft: #333333;
    --card-white: #ffffff;
    --card-fog: #ececec;
    --swoosh-grey: #a9a9a9;
    --swoosh-dark: #262626;
    --swoosh-deep: #151515;
    --night: #050505;
    --night-glow: #2a2a2a;
    --rose-light: #f6eeee;
    --rose-mid: #cfa9ab;
    --rose-deep: #8c4f55;
    --paper-text: #f2f2f2;
    --tag-dark: #3a3a3a;
    --accent: #d3121b;
  }
  * { margin: 0; padding: 0; box-sizing: border-box; }
  html, body {
    width: 969px; height: 1200px; overflow: hidden;
    background: var(--board);
    font-family: "Ubuntu", Arial, sans-serif;
    color: var(--ink);
  }
  .board { position: relative; width: 969px; height: 1200px; }
  .side-label {
    position: absolute; left: 59px;
    font-size: 19px; color: var(--ink);
    transform: translateY(-50%);
  }
  .card {
    position: absolute; overflow: hidden;
    box-shadow: 0 1px 4px rgba(0,0,0,.35);
  }

  /* Front */
  .card--front {
    left: 210px; top: 41px; width: 581px; height: 330px;
    background: radial-gradient(ellipse at 35% 45%, var(--card-white) 40%, var(--card-fog) 100%);
  }
  .card--front .swoosh { position: absolute; inset: 0; }
  .holder-name {
    position: absolute; left: 41px; top: 142px;
    font-size: 29px; font-weight: 400; color: var(--ink);
  }
  .holder-role {
    position: absolute; left: 42px; top: 178px;
    font-size: 16px; color: var(--ink-soft);
  }
  .contact-list {
    position: absolute; left: 42px; top: 219px;
    list-style: none; font-size: 13px; color: var(--ink-soft);
  }
  .contact-list li {
    display: flex; align-items: center; gap: 9px; height: 21.5px;
  }
  .contact-list svg { width: 13px; height: 13px; flex: none; }

  /* Backs */
  .card--back-dark {
    left: 208px; top: 410px; width: 586px; height: 331px;
    background: radial-gradient(ellipse 55% 60% at 50% 48%, var(--night-glow) 0%, var(--night) 100%);
  }
  .card--back-rose {
    left: 207px; top: 816px; width: 587px; height: 334px;
  }
  .card--back-rose .texture {
    position: absolute; inset: 0;
    background:
      radial-gradient(ellipse 60% 55% at 50% 42%, var(--rose-light) 0%, rgba(246,238,238,.6) 45%, rgba(246,238,238,0) 80%),
      linear-gradient(160deg, var(--rose-deep) 0%, var(--rose-mid) 40%, var(--rose-mid) 65%, var(--rose-deep) 100%);
  }
  .wordmark {
    position: absolute; left: 0; right: 0;
    display: flex; justify-content: center; align-items: center; gap: 9px;
    font-size: 18px; font-weight: 700; letter-spacing: .5px;
  }
  .wordmark .mark-dot {
    width: 14px; height: 14px; border-radius: 50%; background: var(--accent);
  }
  .card--back-dark .wordmark { top: 159px; color: var(--paper-text); }
  .card--back-rose .wordmark { top: 152px; color: var(--ink); }
  .tagline {
    position: absolute; left: 0; right: 0; text-align: center;
    font-size: 10px; letter-spacing: 1.4px;
  }
  .card--back-dark .tagline { top: 219px; color: var(--paper-text); }
  .card--back-rose .tagline { top: 209px; color: var(--tag-dark); }
</style>
</head>
<body>
<main class="board">
  <span class="side-label" style="top:214px">Front</span>
  <span class="side-label" style="top:597px">Back opt.1</span>
  <span class="side-label" style="top:1018px">Back opt.2</span>

  <section class="card card--front" aria-label="Card front">
    <svg class="swoosh" viewBox="0 0 581 330" preserveAspectRatio="none" aria-hidden="true">
      <defs>
        <linearGradient id="darkSweep" x1="0" y1="0" x2="1" y2="1">
          <stop offset="0" stop-color="#3a3a3a"/>
          <stop offset=".5" stop-color="#262626"/>
          <stop offset="1" stop-color="#141414"/>
        </linearGradient>
      </defs>
      <path d="M457 0 C370 30 322 100 332 180 C340 250 366 292 372 330 L581 330 L581 0 Z" fill="var(--swoosh-grey)"/>
      <path d="M500 0 C400 28 335 100 345 178 C353 245 390 292 393 330 L581 330 L581 0 Z" fill="url(#darkSweep)"/>
      <path d="M581 40 C520 60 470 110 460 180 C452 240 470 300 480 330 L581 330 Z" fill="var(--swoosh-deep)" opacity=".55"/>
    </svg>

    <h1 class="holder-name">Marcus Feldwick</h1>
    <p class="holder-role">Business Owner</p>
    <ul class="contact-list">
      <li>
        <svg viewBox="0 0 16 16" aria-hidden="true"><path d="M4 1 L6.5 4.5 L5 6.5 C6 8.8 7.2 10 9.5 11 L11.5 9.5 L15 12 L13 15 C7 14.5 1.5 9 1 3 Z" fill="var(--ink)"/></svg>
        <span>0498357162</span>
      </li>
      <li>
        <svg viewBox="0 0 16 16" aria-hidden="true"><rect x="1.5" y="3.5" width="13" height="9" fill="none" stroke="var(--ink-soft)" stroke-width="1.2"/><path d="M1.5 3.5 L8 9 L14.5 3.5" fill="none" stroke="var(--ink-soft)" stroke-width="1.2"/></svg>
        <span>marcusfeldwick@crestlinedeliverypartners.com</span>
      </li>
      <li>
        <svg viewBox="0 0 16 16" aria-hidden="true"><circle cx="8" cy="8" r="6.5" fill="none" stroke="var(--ink-soft)" stroke-width="1.2"/><ellipse cx="8" cy="8" rx="3" ry="6.5" fill="none" stroke="var(--ink-soft)" stroke-width="1"/><path d="M1.5 8 H14.5 M2.8 4.8 H13.2 M2.8 11.2 H13.2" stroke="var(--ink-soft)" stroke-width="1"/></svg>
        <span>www.crestlinedeliverypartners.com.au</span>
      </li>
    </ul>
  </section>

  <section class="card card--back-dark" aria-label="Card back, dark option">
    <div class="wordmark"><span class="mark-dot"></span><span>CRESTLINE DELIVERY PARTNERS</span></div>
    <p class="tagline">Providing | Knowledge | Expertise | Experience</p>
  </section>

  <section class="card card--back-rose" aria-label="Card back, rose option">
    <div class="texture" role="img" aria-label="Soft rose abstract faceted light background"></div>
    <div class="wordmark"><span class="mark-dot"></span><span>CRESTLINE DELIVERY PARTNERS</span></div>
    <p class="tagline">Providing | Knowledge | Expertise | Experience</p>
  </section>
</main>
</body>
</html>
```